looking for sleek business card to standout from the crowd!

We are a young biotechnology company looking to help you personalize your health through understanding your genetic make up. We need you help in making a clean but sleek business card design using our new logo. The goal? Any time we give our cards out, people say "nice card!" The feel we are going for is "modern-techy". We don't want to come across as an old, giant pharma company, but not trying to be a hipster either.

Target Market(s)

healthcare and biotechnology industry.

Industry/Entity Type

Biotechnology

Contact Information for Business Card

Info to include on the card will be NAME, TITLE, EMAIL, PHONE. The companies website (www.corvalinbio.com) should also be on the card some where. Would like the logo, when printed, to be raised.

Requirements
Must have
• The logo we have attached in the color it is in. Fonts for text should lean toward more professional/tech.
Nice to have
• Prefer white/light color background
Should not have
• cartoons, landscape backgrounds images.

```html
<!DOCTYPE html>
<html lang="en">
<head>
<meta charset="utf-8">
<title>Corvalin Business Card</title>
<link href="https://fonts.googleapis.com/css2?family=Montserrat:wght@500;600;700&display=swap" rel="stylesheet">
<style>
  :root {
    --stage: #1c1c1e;
    --brand-blue: #1575be;
    --brand-green: #8cc63f;
    --card-black: #050505;
    --silver: #c9cdd2;
    --graphite: #3a3d42;
    --white: #ffffff;
  }
  * { box-sizing: border-box; margin: 0; padding: 0; }
  html, body {
    width: 1200px; height: 852px; overflow: hidden;
    background: var(--stage);
    font-family: "Montserrat", Arial, sans-serif;
  }
  .stage {
    position: relative; width: 1200px; height: 852px;
    display: flex; align-items: center; justify-content: center; gap: 60px;
  }
  .card {
    position: relative; width: 510px; height: 292px;
    border-radius: 18px; overflow: hidden;
  }
  .card-front { background: var(--brand-blue); display: flex; align-items: center; justify-content: center; }
  .brand { display: flex; align-items: center; gap: 10px; font-weight: 700; letter-spacing: 1px; }
  .card-front .brand-name { color: var(--silver); font-size: 44px; }
  .card-front .brand-dot { width: 38px; height: 38px; border-radius: 50%; background: var(--graphite); }
  .card-back { background: var(--card-black); }
  .card-back .geometry { position: absolute; inset: 0; width: 100%; height: 100%; }
  .card-back .brand { position: absolute; left: 34px; top: 112px; }
  .card-back .brand-name { color: var(--brand-blue); font-size: 34px; }
  .card-back .brand-dot { width: 30px; height: 30px; border-radius: 50%; background: var(--brand-green); }
  .contact { position: absolute; left: 34px; top: 178px; color: var(--white); }
  .contact .name { color: var(--brand-blue); font-size: 15px; font-weight: 700; }
  .contact .title { color: var(--brand-green); font-size: 11px; font-weight: 500; margin-bottom: 6px; }
  .contact ul { list-style: none; }
  .contact li { display: flex; align-items: center; gap: 8px; font-size: 11px; font-weight: 500; line-height: 20px; }
  .contact .icon { width: 13px; height: 13px; flex: none; }
</style>
</head>
<body>
<main class="stage">
  <section class="card card-front">
    <div class="brand"><span class="brand-name">CORVALIN</span><span class="brand-dot"></span></div>
  </section>

  <section class="card card-back">
    <svg class="geometry" viewBox="0 0 510 292" aria-hidden="true">
      <polygon points="290,0 510,0 510,292 395,292" fill="var(--brand-blue)"/>
      <polygon points="345,52 510,178 510,292 440,292" fill="var(--card-black)"/>
      <polygon points="445,205 500,245 455,292 445,292" fill="var(--brand-green)"/>
    </svg>
    <div class="brand"><span class="brand-name">CORVALIN</span><span class="brand-dot"></span></div>
    <div class="contact">
      <p class="name">Marcus Hale</p>
      <p class="title">Managing Director</p>
      <ul>
        <li>
          <svg class="icon" viewBox="0 0 14 14"><circle cx="7" cy="7" r="7" fill="var(--brand-green)"/><path d="M4.5 3.5l1.5 0 .7 1.8-.9.7a5 5 0 0 0 2.2 2.2l.7-.9 1.8.7v1.5c0 .5-.4.8-.9.8A6 6 0 0 1 3.7 4.4c0-.5.3-.9.8-.9z" fill="var(--card-black)"/></svg>
          0741-512-390
        </li>
        <li>
          <svg class="icon" viewBox="0 0 14 14"><circle cx="7" cy="7" r="7" fill="var(--brand-green)"/><rect x="3.5" y="4.5" width="7" height="5" fill="none" stroke="var(--card-black)" stroke-width="1"/><path d="M3.5 4.5l3.5 3 3.5-3" fill="none" stroke="var(--card-black)" stroke-width="1"/></svg>
          corvalinbio.com
        </li>
        <li>
          <svg class="icon" viewBox="0 0 14 14"><circle cx="7" cy="7" r="7" fill="var(--brand-green)"/><circle cx="7" cy="7" r="3.6" fill="none" stroke="var(--card-black)" stroke-width="1"/><path d="M3.4 7h7.2M7 3.4c-1.6 2-1.6 5.2 0 7.2M7 3.4c1.6 2 1.6 5.2 0 7.2" fill="none" stroke="var(--card-black)" stroke-width=".8"/></svg>
          www.corvalinbio.com
        </li>
      </ul>
    </div>
  </section>
</main>
</body>
</html>
```